STOREFRONT SIGNAGE/ NEW LOGO

Looking for someone to enhance my current sign idea. I own a pawn shop , which is also a gun shop. I want a catchy front sign, which will be a lighted box sign. I may want to incorporate some symbols or character symbology that highlight firearms, such as : guns, ammo, targets, scope retical , gold, diamonds, cash, watches and/or pawn balls, and im open to other ideas, but i do not want it too busy, i want it simple, with a twist. Attached, you will find a very basic design, showing the business name and the verbiage that I would like to be incorporated into the design. God bless and thank you. may the best design win !

```html
<!DOCTYPE html>
<html lang="en">
<head>
<meta charset="utf-8">
<title>Meridian Gold &amp; Gun Exchange – Storefront Sign</title>
<link rel="stylesheet" href="https://fonts.googleapis.com/css2?family=Poppins:wght@600;700;800&display=swap">
<style>
  :root {
    --page-bg: #c2c2c2;
    --sign-white: #ffffff;
    --band-dark: #2b2b2b;
    --ink-black: #141414;
    --gold-deep: #a87b1f;
    --gold-light: #f0c65c;
    --red-deep: #d90000;
    --red-bright: #ff1616;
    --check-red: #e3101a;
    --rule-grey: #d6d6d6;
    --brand-gold: #b8862a;
  }
  html, body {
    margin: 0;
    padding: 0;
    width: 1134px;
    height: 1200px;
    overflow: hidden;
    background: var(--page-bg);
  }
  .canvas {
    position: relative;
    width: 1134px;
    height: 1200px;
  }
  .sign {
    position: absolute;
    left: 40px;
    top: 496px;
    width: 1054px;
    height: 207px;
    filter: drop-shadow(4px 6px 5px rgba(0,0,0,0.35));
  }
  .sign svg { display: block; }
  .headline { font-family: "Poppins", sans-serif; font-weight: 800; }
  .tagline { font-family: "Poppins", sans-serif; font-weight: 600; }
  .service { font-family: "Poppins", sans-serif; font-weight: 700; }
  .brand-name { font-family: "Poppins", sans-serif; font-weight: 800; }
</style>
</head>
<body>
<main class="canvas">
  <div class="sign">
    <svg width="1054" height="207" viewBox="0 0 1054 207" xmlns="http://www.w3.org/2000/svg">
      <defs>
        <linearGradient id="gold-band" x1="0" x2="1" y1="0" y2="0">
          <stop offset="0" stop-color="var(--gold-deep)"/>
          <stop offset="0.45" stop-color="var(--gold-light)"/>
          <stop offset="1" stop-color="var(--gold-deep)"/>
        </linearGradient>
        <linearGradient id="red-band" x1="0" x2="1" y1="0" y2="0">
          <stop offset="0" stop-color="var(--red-deep)"/>
          <stop offset="0.5" stop-color="var(--red-bright)"/>
          <stop offset="1" stop-color="var(--red-deep)"/>
        </linearGradient>
        <clipPath id="centre-panel">
          <path d="M166,0 L889,0 Q808,103 886,207 L170,207 Q248,103 166,0 Z"/>
        </clipPath>
      </defs>

      <!-- base -->
      <rect class="sign-base" width="1054" height="207" fill="var(--sign-white)"/>

      <!-- centre panel -->
      <g class="centre-panel" clip-path="url(#centre-panel)">
        <rect class="gold-band" x="150" y="0" width="380" height="143" fill="url(#gold-band)"/>
        <rect class="red-band" x="529" y="0" width="380" height="143" fill="url(#red-band)"/>
        <rect class="dark-band" x="150" y="143" width="760" height="64" fill="var(--band-dark)"/>
      </g>
      <path class="panel-edge" d="M166,0 Q248,103 170,207" fill="none" stroke="var(--band-dark)" stroke-width="2.5"/>
      <path class="panel-edge" d="M889,0 Q808,103 886,207" fill="none" stroke="var(--band-dark)" stroke-width="2.5"/>

      <!-- brand -->
      <g class="brand">
        <circle class="brand-dot" cx="94" cy="82" r="42" fill="var(--brand-gold)"/>
        <text class="brand-name" x="94" y="172" text-anchor="middle" font-size="17" letter-spacing="1" fill="var(--brand-gold)">MERIDIAN</text>
      </g>

      <!-- headlines -->
      <text class="headline" x="244" y="83" font-size="68" letter-spacing="-1.5" fill="var(--ink-black)">GOLD</text>
      <text class="headline" x="245" y="119" font-size="44" letter-spacing="-1" fill="var(--ink-black)">EXCHANGE</text>

      <text class="headline" x="813" y="83" text-anchor="end" font-size="68" letter-spacing="-1.5" fill="var(--sign-white)">GUN</text>
      <text class="headline" x="813" y="119" text-anchor="end" font-size="44" letter-spacing="-1" fill="var(--sign-white)">EXCHANGE</text>

      <g class="ampersand-badge">
        <circle cx="530" cy="69" r="28" fill="var(--sign-white)"/>
        <text class="tagline" x="530" y="83" text-anchor="middle" font-size="38" fill="var(--ink-black)">&amp;</text>
      </g>

      <!-- tagline -->
      <text class="tagline" x="531" y="186" text-anchor="middle" font-size="30" letter-spacing="0.3" fill="var(--sign-white)">CA$H FOR GOLD  |  CA$H FOR GUNS</text>

      <!-- services list -->
      <g class="services">
        <g class="service-item" transform="translate(0,40)">
          <circle cx="906" cy="0" r="9" fill="var(--check-red)"/>
          <path d="M901.5,0.5 L905,4 L911,-3.5" fill="none" stroke="#fff" stroke-width="2.4" stroke-linecap="round" stroke-linejoin="round"/>
          <text class="service" x="921" y="6.5" font-size="18" fill="var(--ink-black)">PAWN</text>
          <line x1="921" y1="18" x2="1018" y2="18" stroke="var(--rule-grey)" stroke-width="1"/>
        </g>
        <g class="service-item" transform="translate(0,73)">
          <circle cx="906" cy="0" r="9" fill="var(--check-red)"/>
          <path d="M901.5,0.5 L905,4 L911,-3.5" fill="none" stroke="#fff" stroke-width="2.4" stroke-linecap="round" stroke-linejoin="round"/>
          <text class="service" x="921" y="6.5" font-size="18" fill="var(--ink-black)">BUY</text>
          <line x1="921" y1="18" x2="1018" y2="18" stroke="var(--rule-grey)" stroke-width="1"/>
        </g>
        <g class="service-item" transform="translate(0,107)">
          <circle cx="906" cy="0" r="9" fill="var(--check-red)"/>
          <path d="M901.5,0.5 L905,4 L911,-3.5" fill="none" stroke="#fff" stroke-width="2.4" stroke-linecap="round" stroke-linejoin="round"/>
          <text class="service" x="921" y="6.5" font-size="18" fill="var(--ink-black)">SELL</text>
          <line x1="921" y1="18" x2="1018" y2="18" stroke="var(--rule-grey)" stroke-width="1"/>
        </g>
        <g class="service-item" transform="translate(0,140)">
          <circle cx="906" cy="0" r="9" fill="var(--check-red)"/>
          <path d="M901.5,0.5 L905,4 L911,-3.5" fill="none" stroke="#fff" stroke-width="2.4" stroke-linecap="round" stroke-linejoin="round"/>
          <text class="service" x="921" y="6.5" font-size="18" fill="var(--ink-black)">TRADE</text>
          <line x1="921" y1="18" x2="1018" y2="18" stroke="var(--rule-grey)" stroke-width="1"/>
        </g>
        <g class="service-item" transform="translate(0,173)">
          <circle cx="906" cy="0" r="9" fill="var(--check-red)"/>
          <path d="M901.5,0.5 L905,4 L911,-3.5" fill="none" stroke="#fff" stroke-width="2.4" stroke-linecap="round" stroke-linejoin="round"/>
          <text class="service" x="921" y="6.5" font-size="18" fill="var(--ink-black)">LAYAWAY</text>
        </g>
      </g>
    </svg>
  </div>
</main>
</body>
</html>
```